Marlow Bay Kestrel Arrivals Flyer

A 2 sided DL size flyer. (Approx 20cm long by 10cm wide)
That has logo and blurb about company on front. On back details of Kestrel arrivals package, trademark, contact details and license numbers.
We feel we need to see the text on the flyer design and then make some changes so there will be some back and forth about written content. There may be a reduction in the amount of text we want for the blurb about the company but the rest is mandatory.
Our logo is blue and green, we do not want a white flyer with black text as feel this looks homemade so we need your suggestions about what colour the text and flyer could be.
We want the flyer to look clean and modern. It will go on a stand at an immigration fair and will be sent in the post and via email to clients. We will need posters at a later stage.
Migrants
It Company

```html
<!DOCTYPE html>
<html lang="en">
<head>
<meta charset="utf-8">
<title>Marlow Bay Kestrel Arrivals – DL Flyer</title>
<link rel="stylesheet" href="https://fonts.googleapis.com/css2?family=Audiowide&family=Merriweather:wght@400;900&family=Montserrat:wght@600&family=Roboto+Condensed:wght@300;400;700&display=swap">
<style>
  :root{
    --canvas:#e4e4e4;
    --blue:#1765b0;
    --blue-deep:#0d4f95;
    --blue-light:#2a7fd0;
    --green:#4cc13c;
    --green-text:#5fd33a;
    --ribbon-green:#3f9a2e;
    --navy:#163a66;
    --quote:#173050;
    --white:#ffffff;
    --ink:#1b1b1b;
  }
  *{box-sizing:border-box;margin:0;padding:0}
  html,body{width:1200px;height:1200px;overflow:hidden;background:var(--canvas)}
  body{position:relative;font-family:"Roboto Condensed",sans-serif}

  .page{position:absolute;top:82px;width:517px;height:1036px;overflow:hidden;
        box-shadow:0 4px 14px rgba(0,0,0,.25)}
  .page--front{left:70px}
  .page--back{left:607px}
  .page-art{position:absolute;inset:0;width:100%;height:100%}

  /* brand lockup */
  .brand{position:absolute;left:54px;top:36px;display:flex;align-items:center}
  .brand__dot{width:93px;height:93px;border-radius:50%;flex:none}
  .brand__rule{width:2px;height:104px;margin:0 12px 0 27px}
  .brand__name{font-family:"Audiowide",sans-serif;font-size:27px;line-height:30px}
  .brand__tag{font-size:17px;letter-spacing:5.5px;margin-top:6px;font-weight:400}
  .page--front .brand__dot{background:var(--green)}
  .page--front .brand__rule{background:var(--ink)}
  .page--front .brand__name{color:var(--blue)}
  .page--front .brand__tag{color:var(--ink)}
  .page--back .brand__dot{background:var(--white)}
  .page--back .brand__rule{background:var(--white)}
  .page--back .brand__name,.page--back .brand__tag{color:var(--white)}

  .pill{position:absolute;left:84px;width:352px;height:29px;border-radius:15px;
        background:linear-gradient(#ffffff,#d8d8d8);color:var(--blue-deep);
        font-weight:700;font-size:18px;text-align:center;line-height:29px;
        box-shadow:0 3px 6px rgba(0,0,0,.3)}

  .headline-frame{position:absolute;left:26px;top:494px;width:465px;height:62px;
        border:1px solid rgba(255,255,255,.6);border-top:none}
  .headline-frame::before,.headline-frame::after{content:"";position:absolute;top:0;height:1px;
        background:rgba(255,255,255,.6);width:58px}
  .headline-frame::before{left:0}
  .headline-frame::after{right:0}
  .headline-top{position:absolute;left:0;width:517px;top:481px;text-align:center;
        font-family:"Audiowide",sans-serif;font-size:20px;color:var(--white);font-weight:400}
  .headline-main{position:absolute;left:0;width:517px;top:512px;text-align:center;
        font-family:"Audiowide",sans-serif;font-size:30px;color:var(--green-text);letter-spacing:.5px}

  .copy{position:absolute;left:26px;width:465px;color:var(--white);font-weight:300;
        font-size:14px;line-height:17.6px;text-align:justify;text-align-last:center}
  .copy b{font-weight:700}
  .copy--center{text-align:center}

  .quote-mark{position:absolute;left:34px;top:733px;font-family:"Merriweather",serif;
        font-size:100px;line-height:1;color:var(--quote);font-weight:900}

  .ribbon{position:absolute;left:26px;width:465px;display:flex;align-items:center;justify-content:center;
        text-align:center;font-family:"Merriweather",serif;color:var(--ribbon-green);
        font-size:15.5px;line-height:20px;
        background:linear-gradient(#ffffff,#dcdcdc);
        clip-path:polygon(0 0,100% 0,96% 50%,100% 100%,0 100%,4% 50%)}

  .web{position:absolute;left:0;width:517px;top:983px;display:flex;justify-content:center;align-items:center;
        font-family:"Montserrat",sans-serif;font-weight:600;font-size:18px;letter-spacing:2px;color:var(--navy)}
  .web__dot{width:12px;height:12px;border-radius:50%;background:var(--navy);margin-right:10px}

  .benefits{position:absolute;left:35px;top:294px;width:460px;list-style:none}
  .benefits li{position:absolute;left:0;display:flex;color:var(--white);font-weight:300;font-size:14px;line-height:17.6px}
  .benefits svg{flex:none;width:15px;height:15px;margin:1px 8px 0 0}

  .choice{position:absolute;top:622px;width:141px;height:124px;border:1px solid rgba(255,255,255,.75);
        color:var(--white);font-weight:300;font-size:13px;line-height:18px;text-align:center;
        padding-top:23px}
  .choice__num{position:absolute;top:-20px;left:50%;transform:translateX(-50%);width:34px;height:34px;
        border-radius:50%;background:var(--white);border:3px solid var(--green);color:var(--ribbon-green);
        font-family:"Audiowide",sans-serif;font-size:18px;line-height:28px;text-align:center}

  .contacts{position:absolute;left:0;width:517px;top:821px;text-align:center;color:var(--white);
        font-weight:700;font-size:19.5px;line-height:24px}
  .email{position:absolute;left:0;width:517px;top:902px;text-align:center;color:var(--white);
        font-weight:400;font-size:16px}
  .email-icon{position:absolute;left:246px;top:881px;width:17px;height:17px}
  .badge{position:absolute;left:31px;top:884px;width:92px;height:92px;border-radius:50%;
        background:#b7bd7c;border:5px solid #dfe3b8;box-shadow:0 0 0 4px var(--green)}
</style>
</head>
<body>

<!-- FRONT -->
<section class="page page--front">
  <svg class="page-art" viewBox="0 0 517 1036" preserveAspectRatio="none">
    <defs>
      <linearGradient id="fBody" x1="0" y1="0" x2="0" y2="1">
        <stop offset="0" stop-color="#1a6cbc"/><stop offset="1" stop-color="#0f5299"/>
      </linearGradient>
      <linearGradient id="fPaper" x1="0" y1="0" x2="0" y2="1">
        <stop offset="0" stop-color="#fbfbfb"/><stop offset="1" stop-color="#dedede"/>
      </linearGradient>
      <linearGradient id="fScene" x1="0" y1="0" x2="0" y2="1">
        <stop offset="0" stop-color="#6f9fd6"/>
        <stop offset=".3" stop-color="#9ab7d4"/>
        <stop offset=".48" stop-color="#4a6f8e"/>
        <stop offset=".6" stop-color="#2b6bb3"/>
        <stop offset=".75" stop-color="#3d8a2c"/>
        <stop offset="1" stop-color="#69b545"/>
      </linearGradient>
    </defs>
    <rect width="517" height="1036" fill="url(#fBody)"/>
    <path d="M0 0H517V100C400 150 200 200 0 150Z" fill="url(#fPaper)"/>
    <path d="M0 152C200 202 400 152 517 102V112C400 165 200 212 0 164Z" fill="var(--green)"/>
    <path d="M0 164C200 212 400 165 517 112V122C400 175 200 222 0 174Z" fill="var(--blue-light)"/>
    <path role="img" aria-label="Photo of a New Zealand lake with snowy mountains and green vineyards"
          d="M0 174C200 222 400 175 517 122V446C400 400 200 392 0 440Z" fill="url(#fScene)"/>
    <path d="M0 440C200 392 400 400 517 446V452C400 410 200 402 0 448Z" fill="#ffffff"/>
    <path d="M0 448C200 402 400 410 517 452V468C400 426 200 420 0 480Z" fill="var(--green)"/>
    <path d="M0 892C150 940 380 955 517 880V896C380 968 150 958 0 912Z" fill="var(--green)"/>
    <path d="M0 912C150 958 380 968 517 896V904C380 978 150 968 0 920Z" fill="var(--blue-light)"/>
    <path d="M0 920C150 968 380 978 517 904V1036H0Z" fill="url(#fPaper)"/>
  </svg>

  <div class="brand">
    <div class="brand__dot"></div>
    <div class="brand__rule"></div>
    <div>
      <div class="brand__name">Marlow Bay<br>Kestrel Arrivals</div>
      <div class="brand__tag">Immigration Advice</div>
    </div>
  </div>

  <div class="headline-frame"></div>
  <div class="headline-top">Friendly &amp; helpful Licensed</div>
  <div class="headline-main">IMMIGRATION ADVISERS</div>

  <div class="pill" style="top:562px">We facilitate fast and problem free visas</div>

  <p class="copy" style="top:616px"><b>Marlow Bay Kestrel Arrivals</b> is a family business; headed by two sisters Ada and Maren Holloway. Originally from the UK they migrated to New Zealand over ten years ago, so understand how it feels to move to a new country &amp; go through the visa process.</p>
  <p class="copy" style="top:696px"><b>Maren &amp; Ada</b> are passionate about what New Zealand has to offer and enjoy the chance to help people make their home here. They work across all types of visa applications – <b>to live, work or study.</b></p>

  <div class="ribbon" style="top:774px;height:66px">Working closely with you to meet your immigration<br>goals, we help and guide you at every stage.</div>
  <div class="quote-mark">&ldquo;</div>

  <p class="copy copy--center" style="top:862px">Trained and qualified, they have specialist knowledge of the immigration system.<br>Able to work to urgent timeframes or with clients who have<br>character or health issues.</p>

  <div class="web"><span class="web__dot"></span>www.kestrelarrivals.example</div>
</section>

<!-- BACK -->
<section class="page page--back">
  <svg class="page-art" viewBox="0 0 517 1036" preserveAspectRatio="none" aria-hidden="true">
    <defs>
      <linearGradient id="bBody" x1="0" y1="0" x2="0" y2="1">
        <stop offset="0" stop-color="#1766b4"/><stop offset="1" stop-color="#0f5299"/>
      </linearGradient>
      <linearGradient id="bPaper" x1="0" y1="0" x2="0" y2="1">
        <stop offset="0" stop-color="#fbfbfb"/><stop offset="1" stop-color="#dedede"/>
      </linearGradient>
    </defs>
    <rect width="517" height="1036" fill="url(#bBody)"/>
    <path d="M0 892C150 940 380 955 517 880V896C380 968 150 958 0 912Z" fill="var(--green)"/>
    <path d="M0 912C150 958 380 968 517 896V904C380 978 150 968 0 920Z" fill="var(--blue-light)"/>
    <path d="M0 920C150 968 380 978 517 904V1036H0Z" fill="url(#bPaper)"/>
  </svg>

  <div class="brand">
    <div class="brand__dot"></div>
    <div class="brand__rule"></div>
    <div>
      <div class="brand__name">Marlow Bay<br>Kestrel Arrivals</div>
      <div class="brand__tag">Immigration Advice</div>
    </div>
  </div>

  <div class="pill" style="top:150px">Kestrel Arrivals Package</div>

  <p class="copy copy--center" style="top:202px;left:34px;width:449px">Set yourself on a clear pathway from your first student visa to permanent residency with our comprehensive immigration package. Connect with licensed advisers who walk alongside you in your New Zealand journey, helping to make the most of your time and money</p>

  <ul class="benefits">
    <li style="top:0"><svg viewBox="0 0 16 16"><circle cx="8" cy="8" r="7" fill="none" stroke="#4cc13c" stroke-width="2"/><path d="M4.5 8.3l2.3 2.3 4.7-5" fill="none" stroke="#fff" stroke-width="1.8"/></svg>Confirmed, discounted rates for ongoing visas once your study is completed.</li>
    <li style="top:35px"><svg viewBox="0 0 16 16"><circle cx="8" cy="8" r="7" fill="none" stroke="#4cc13c" stroke-width="2"/><path d="M4.5 8.3l2.3 2.3 4.7-5" fill="none" stroke="#fff" stroke-width="1.8"/></svg>A one on one session with a licensed adviser to plan how to maximise your<br>studies &amp; work opportunities to achieve residency faster.</li>
    <li style="top:87px"><svg viewBox="0 0 16 16"><circle cx="8" cy="8" r="7" fill="none" stroke="#4cc13c" stroke-width="2"/><path d="M4.5 8.3l2.3 2.3 4.7-5" fill="none" stroke="#fff" stroke-width="1.8"/></svg>Attendance at an immigration seminar.</li>
    <li style="top:122px"><svg viewBox="0 0 16 16"><circle cx="8" cy="8" r="7" fill="none" stroke="#4cc13c" stroke-width="2"/><path d="M4.5 8.3l2.3 2.3 4.7-5" fill="none" stroke="#fff" stroke-width="1.8"/></svg>Vital updates on immigration policy changes &amp; how they impact on you.</li>
    <li style="top:157px"><svg viewBox="0 0 16 16"><circle cx="8" cy="8" r="7" fill="none" stroke="#4cc13c" stroke-width="2"/><path d="M4.5 8.3l2.3 2.3 4.7-5" fill="none" stroke="#fff" stroke-width="1.8"/></svg>Access immediate advice from someone who knows your situation if things<br>go wrong.</li>
  </ul>

  <div class="ribbon" style="top:511px;height:67px">Our Kestrel Arrivals Package includes<br>3 visa applications, choose from:</div>

  <div class="choice" style="left:26px"><span class="choice__num">1</span>Deposit of 15%<br>which covers<br>Post Study Open<br>Visa (job search)</div>
  <div class="choice" style="left:188px"><span class="choice__num">2</span>Either Post Study<br>Employer Assisted Visa<br>or Essential Skills Work<br>Visa - (this includes<br>employer support)</div>
  <div class="choice" style="left:350px"><span class="choice__num">3</span>Either Skilled Migrant<br>Category Residence or<br>Work to Residence Visa<br>(both components for<br>latter)</div>

  <p class="copy copy--center" style="top:766px;font-weight:400;font-size:13px">Add on's for family and work options available.</p>
  <p class="copy copy--center" style="top:785px;font-weight:700;font-size:14.5px">Let Marlow Bay Kestrel Arrivals plan your route to residency.</p>

  <div class="contacts">Maren 021 555 0148 License Number 209900117<br>Ada 021 555 01927 License Number 209900245</div>

  <svg class="email-icon" viewBox="0 0 18 18" aria-hidden="true"><circle cx="9" cy="9" r="9" fill="#4cc13c"/><rect x="4.5" y="5.8" width="9" height="6.4" fill="none" stroke="#fff" stroke-width="1.3"/><path d="M4.5 6l4.5 3.6L13.5 6" fill="none" stroke="#fff" stroke-width="1.3"/></svg>
  <div class="email">hello@kestrelarrivals.example</div>

  <div class="badge" role="img" aria-label="Adviser licensing badge"></div>

  <div class="web"><span class="web__dot"></span>www.kestrelarrivals.example</div>
</section>

</body>
</html>
```